Wellness Company needs 2 updated pages for our powerpoint

1 page of our powerpoint needs to be split into 2 pages. I have uploaded an image of it all on 1 page, the left side needs to be on 1 page and the right side needs to be on a separate page. I also uploaded images of the top & bottom since it is so blurry. Landscape view, please. Don't worry about the bottom of the page design since that is our template.

Target Market(s)

Wellness and Business

Industry/Entity Type

Health And Wellness

Requirements
Must have
• Clear wording and bold font.
Nice to have
• Clear circles and images

```html
<!DOCTYPE html>
<html lang="en">
<head>
<meta charset="utf-8">
<title>Leafline Wellness – Compensation Plan at a Glance</title>
<link rel="stylesheet" href="https://fonts.googleapis.com/css2?family=Bebas+Neue&family=Source+Sans+3:wght@300;400;600;700&display=swap">
<style>
  :root {
    --bg: #e9e8e6;
    --paper: #ffffff;
    --green: #62a846;
    --green-light: #8dc63f;
    --green-dark: #4f9a3a;
    --orange: #f2b01e;
    --orange-deep: #f39021;
    --slate: #4d4f4e;
    --ink: #4a4a4a;
    --muted: #9a9a9a;
  }
  * { box-sizing: border-box; margin: 0; padding: 0; }
  html, body { width: 772px; height: 1200px; overflow: hidden; background: var(--bg); }
  body { position: relative; font-family: "Source Sans 3", Arial, sans-serif; color: var(--ink); }

  .slide { position: absolute; left: 89px; width: 603px; height: 453px; background: var(--paper); box-shadow: 0 3px 10px rgba(0,0,0,.25); }
  .slide--overview { top: 115px; }
  .slide--levels { top: 655px; }
  .abs { position: absolute; }

  .brand { left: 22px; top: 28px; display: flex; align-items: center; gap: 8px; color: var(--green); font-weight: 700; font-size: 19px; line-height: 1.05; letter-spacing: .5px; }
  .brand-dot { width: 34px; height: 34px; border-radius: 50%; background: var(--green-light); }

  .slide-title { left: 21px; font-family: "Bebas Neue", sans-serif; font-size: 21px; color: var(--orange); letter-spacing: .2px; width: 199px; border-bottom: 1px solid var(--green); padding-bottom: 3px; line-height: 1; }
  .slide--overview .slide-title { top: 113px; }
  .slide--levels .slide-title { top: 22px; }

  .feature-icon { width: 42px; height: 42px; border-radius: 50%; background: radial-gradient(circle at 40% 35%, var(--green-light), var(--green)); box-shadow: 0 0 0 2px #eef3ea, 0 4px 4px rgba(0,0,0,.15); }
  .feature-title { font-size: 15px; color: var(--green); font-weight: 400; }
  .feature-sub { font-size: 10px; color: var(--orange); }
  .feature-copy { font-size: 8px; color: var(--ink); line-height: 1.25; }
  .price-table { left: 78px; top: 217px; width: 96px; font-size: 7.6px; }
  .price-row { display: flex; justify-content: space-between; line-height: 1.3; }
  .price-row span:last-child { width: 26px; }
  .price-row--total { border-top: 1px solid #999; margin-top: 3px; padding-top: 2px; color: var(--green); font-weight: 600; }

  .tier { position: absolute; width: 120px; background: var(--paper); box-shadow: 0 2px 6px rgba(0,0,0,.15); text-align: center; }
  .tier-head { height: 46px; display: flex; align-items: center; justify-content: center; color: #fff; font-size: 13px; font-weight: 600; }
  .tier--mbq { left: 235px; top: 114px; height: 251px; }
  .tier--mbq .tier-head { background: var(--green-light); }
  .tier--sbo { left: 354px; top: 104px; height: 278px; z-index: 2; }
  .tier--sbo .tier-head { background: var(--orange); height: 63px; padding-top: 18px; }
  .tier--ebo { left: 474px; top: 114px; height: 251px; }
  .tier--ebo .tier-head { background: var(--green); }
  .tier-prices { display: flex; justify-content: center; gap: 5px; margin-top: 20px; }
  .tier--sbo .tier-prices { margin-top: 13px; }
  .tier-price { width: 30px; height: 12px; border: 1px solid var(--green); font-size: 5.5px; line-height: 10px; color: var(--muted); }
  .tier-price:nth-child(2) { color: var(--orange); font-weight: 600; }
  .tier-price:nth-child(3) { color: #333; font-weight: 600; }
  .tier-copy { margin-top: 12px; font-size: 7.8px; line-height: 12.4px; color: #555; padding: 0 8px; }

  .footer-band { position: absolute; left: 0; bottom: 0; width: 603px; height: 18px; }

  .level-chart { left: 21px; top: 85px; }
  .level-points { left: 22px; top: 282px; list-style: none; }
  .level-points li { position: relative; padding-left: 16px; font-size: 12px; color: var(--orange); line-height: 19.8px; }
  .level-points li::before { content: ""; position: absolute; left: 0; top: 5px; width: 8px; height: 8px; border: 1px solid var(--green); border-radius: 50%; }

  .quals { position: absolute; left: 335px; top: 0; width: 259px; height: 417px; }
  .quals-bg { position: absolute; inset: 0; }
  .quals-title { position: absolute; top: 24px; width: 100%; text-align: center; font-family: "Bebas Neue", sans-serif; font-size: 20px; color: #fff; }
  .qual { position: absolute; left: 0; width: 259px; color: #fff; }
  .qual-head { position: relative; padding-left: 23px; font-size: 10px; font-weight: 600; letter-spacing: .1px; }
  .qual-head::before { content: ""; position: absolute; left: 0; top: -2px; width: 20px; height: 15px; background: var(--orange); clip-path: polygon(0 0, 75% 0, 100% 50%, 75% 100%, 0 100%); }
  .qual ul { list-style: none; margin-top: 3px; }
  .qual li { position: relative; padding-left: 31px; font-size: 7.6px; line-height: 11.8px; font-weight: 300; }
  .qual li::before { content: ""; position: absolute; left: 23px; top: 3px; width: 5px; height: 5px; border-radius: 50%; background: var(--orange); }
  .quals-note { position: absolute; top: 392px; width: 100%; text-align: center; font-size: 5.6px; line-height: 8px; color: #fff; }
</style>
</head>
<body>

<section class="slide slide--overview">
  <div class="abs brand"><span class="brand-dot"></span><span>LEAFLINE<br>WELLNESS</span></div>
  <h1 class="abs slide-title">Compensation Plan at a Glance</h1>

  <div class="abs feature-icon" style="left:20px;top:175px">
    <svg width="42" height="42" viewBox="0 0 42 42" aria-hidden="true">
      <rect x="11" y="20" width="3" height="9" fill="#fff"/><rect x="15" y="16" width="3" height="13" fill="#fff"/>
      <circle cx="26" cy="22" r="7" fill="#fff"/><path d="M26 22 L26 15 A7 7 0 0 1 33 22 Z" fill="var(--green)"/>
    </svg>
  </div>
  <h2 class="abs feature-title" style="left:76px;top:180px">Direct Seling</h2>
  <p class="abs feature-sub" style="left:76px;top:199px">Sell the product. Keep the profit.</p>
  <div class="abs price-table">
    <div class="price-row"><span>Suggested Retail:</span><span>$34.95</span></div>
    <div class="price-row"><span>Wholesale:</span><span>$24.95</span></div>
    <div class="price-row price-row--total"><span>You keep:</span><span>$10.00</span></div>
  </div>

  <div class="abs feature-icon" style="left:20px;top:289px">
    <svg width="42" height="42" viewBox="0 0 42 42" aria-hidden="true">
      <rect x="10" y="25" width="3" height="6" fill="#fff"/><rect x="15" y="22" width="3" height="9" fill="#fff"/>
      <rect x="20" y="19" width="3" height="12" fill="#fff"/><rect x="25" y="16" width="3" height="15" fill="#fff"/>
      <path d="M10 21 L18 15 L22 17 L31 10" stroke="#fff" stroke-width="2" fill="none"/><path d="M28 9 L32 9 L32 13 Z" fill="#fff"/>
    </svg>
  </div>
  <h2 class="abs feature-title" style="left:76px;top:289px">Fast Start Bonus</h2>
  <p class="abs feature-copy" style="left:77px;top:310px">Eatn up to $40 for each silver, gold<br>or platinum package you sell</p>
  <svg class="abs" style="left:80px;top:333px" width="140" height="50" viewBox="0 0 140 50" aria-label="Fast start bonus tree">
    <g fill="none" stroke="var(--green)" stroke-width=".8">
      <path d="M15 31 V13 H55 M85 13 H115 V31 M65 23 V31"/>
      <circle cx="65" cy="13" r="10"/><circle cx="16" cy="41" r="10"/><circle cx="65" cy="41" r="10"/><circle cx="115" cy="41" r="10"/>
    </g>
    <g font-family="Source Sans 3, sans-serif" font-size="8" text-anchor="middle">
      <text x="65" y="16" fill="var(--green)" font-size="7">YOU</text>
      <text x="16" y="44" fill="var(--muted)">$10</text>
      <text x="65" y="44" fill="var(--orange)" font-weight="600">$20</text>
      <text x="115" y="44" fill="#333" font-weight="600">$40</text>
    </g>
  </svg>

  <article class="tier tier--mbq">
    <header class="tier-head">MBQ</header>
    <div class="tier-prices"><span class="tier-price">$10</span><span class="tier-price">$20</span><span class="tier-price">$40</span></div>
    <p class="tier-copy">MBOs earn up to $10. $20 or $40 per enroliment package sold.</p>
  </article>
  <article class="tier tier--sbo">
    <header class="tier-head">SBO</header>
    <div class="tier-prices"><span class="tier-price">$20</span><span class="tier-price">$40</span><span class="tier-price">$80</span></div>
    <p class="tier-copy">SBOs earn up to $20, $40 or $80 for every enrolliment package sold.<br>SBO leadership bonus may be split between different leaders.<br>MBOs and SBOs will split the difference between bonuses.</p>
  </article>
  <article class="tier tier--ebo">
    <header class="tier-head">EBO</header>
    <div class="tier-prices"><span class="tier-price">$40</span><span class="tier-price">$80</span><span class="tier-price">$160</span></div>
    <p class="tier-copy">EBOs earn up to $40, $80 or $160 for every enroliment package sold.<br>EBO leadership bonus may be split between different leaders.<br>MBOs, SBOs and EBOs will split the difference between bonuses.</p>
  </article>

  <svg class="footer-band" viewBox="0 0 603 18" aria-hidden="true">
    <polygon points="0,0 384,0 380,18 0,18" fill="var(--slate)"/>
    <polygon points="388,0 441,0 437,18 384,18" fill="var(--green)"/>
    <polygon points="445,0 498,0 494,18 441,18" fill="var(--green)"/>
    <polygon points="502,0 555,0 551,18 498,18" fill="var(--green)"/>
    <polygon points="559,0 603,0 603,18 555,18" fill="var(--orange-deep)"/>
  </svg>
</section>

<section class="slide slide--levels">
  <h1 class="abs slide-title">Compensation Plan at a Glance</h1>

  <svg class="abs level-chart" width="300" height="150" viewBox="0 0 300 150" aria-label="Commission levels by rank">
    <g font-family="Source Sans 3, sans-serif" font-size="12" fill="var(--orange)" text-anchor="middle">
      <text x="45" y="10">IBO</text><text x="114" y="10">MBO</text><text x="181" y="10">SBO</text><text x="256" y="10">EBO/REBO</text>
    </g>
    <g stroke="var(--green-light)" stroke-width=".8">
      <line x1="0" y1="36" x2="290" y2="36"/><line x1="0" y1="51" x2="290" y2="51"/><line x1="0" y1="67" x2="290" y2="67"/>
      <line x1="0" y1="82" x2="290" y2="82"/><line x1="0" y1="97" x2="290" y2="97"/><line x1="0" y1="113" x2="290" y2="113"/>
      <line x1="0" y1="128" x2="290" y2="128"/><line x1="0" y1="144" x2="290" y2="144"/>
    </g>
    <g font-family="Source Sans 3, sans-serif" font-size="11" fill="var(--orange)">
      <text x="2" y="34">1</text><text x="2" y="49">2</text><text x="2" y="65">3</text><text x="2" y="80">4</text>
      <text x="2" y="95">5</text><text x="2" y="111">6</text><text x="2" y="126">7</text><text x="2" y="142">8</text>
    </g>
    <rect x="12" y="20" width="68" height="31" fill="var(--green)"/>
    <rect x="82" y="20" width="68" height="62" fill="var(--green)"/>
    <rect x="152" y="20" width="68" height="93" fill="var(--green)"/>
    <rect x="223" y="20" width="68" height="108" fill="var(--green)"/>
    <rect x="223" y="128" width="68" height="16" fill="var(--orange)"/>
    <g font-family="Source Sans 3, sans-serif" font-size="12" fill="#fff" text-anchor="middle">
      <text x="46" y="40">5%</text><text x="116" y="55">5%</text><text x="186" y="71">5%</text><text x="257" y="79">5%</text><text x="257" y="141">10%</text>
    </g>
  </svg>

  <ul class="abs level-points">
    <li>IBOs earn 5% commission on all sales 2 levels deep.</li>
    <li>MBOs earn 5% commission on all sales 4 levels deep.</li>
    <li>SBOs earn 5% commission on all sales 6 levels deep.</li>
    <li>EBOs earn 5% commission on all sales 7 levels deep<br>and 10% on the 8th level.</li>
  </ul>

  <aside class="quals">
    <svg class="quals-bg" viewBox="0 0 259 417" preserveAspectRatio="none" aria-hidden="true">
      <defs><radialGradient id="qualGlow" cx="55%" cy="30%" r="75%"><stop offset="0" stop-color="var(--green-light)"/><stop offset="1" stop-color="var(--green)"/></radialGradient></defs>
      <polygon points="0,0 259,0 259,406 129,417 0,406" fill="url(#qualGlow)"/>
    </svg>
    <h2 class="quals-title">Qualifications</h2>

    <div class="qual" style="top:84px">
      <h3 class="qual-head">INDEPENDENT BUSINESS OWNER (IBO)</h3>
      <ul><li>Enroll as an Active Independent Business Owner</li>
      <li>After your first month to remain active you must personally maintain a minimum of 25 business volume &amp; subscribe to autoship.</li></ul>
    </div>
    <div class="qual" style="top:142px">
      <h3 class="qual-head">MANAGING BUSINESS OWNER (MBO)</h3>
      <ul><li>Be an active IBO and personally maintain 50 business volume</li>
      <li>Personally Sponsor 3 IBO’s. Each of them must be active.</li></ul>
    </div>
    <div class="qual" style="top:196px">
      <h3 class="qual-head">SENIOR BUSINESS OWNER (SBO)</h3>
      <ul><li>Be an Active IBO and personally acquire 100 business volume</li>
      <li>Promote 3 MBO’s in 3 Separate Legs</li>
      <li>Maintain 1500 combined business volume for entire downline</li></ul>
    </div>
    <div class="qual" style="top:261px">
      <h3 class="qual-head">EXECUTIVE BUSINESS OWNER (EBO)</h3>
      <ul><li>Be an Active IBO and personally maintain 200 business volume</li>
      <li>Promote 3 SBO’s in 3 Separate Legs</li>
      <li>Maintain 5000 combined business volume for entire downline</li></ul>
    </div>
    <div class="qual" style="top:326px">
      <h3 class="qual-head">REGIONAL EXECUTIVE BUSINESS OWNER (REBO)</h3>
      <ul><li>Be an Active IBO and personally maintain 400 business volume</li>
      <li>Promote 3 EBO’s in 3 Separate Legs</li>
      <li>Maintain 15000 combined business volume for entire downline</li></ul>
    </div>
    <p class="quals-note">*All requirements must be met to stay commissionable within that rank<br>This is an example only, see full comp plan for details.</p>
  </aside>

  <svg class="footer-band" viewBox="0 0 603 18" aria-hidden="true">
    <polygon points="0,0 384,0 380,18 0,18" fill="var(--slate)"/>
    <polygon points="388,0 441,0 437,18 384,18" fill="var(--green)"/>
    <polygon points="445,0 498,0 494,18 441,18" fill="var(--green)"/>
    <polygon points="502,0 555,0 551,18 498,18" fill="var(--green)"/>
    <polygon points="559,0 603,0 603,18 555,18" fill="var(--orange-deep)"/>
  </svg>
</section>

</body>
</html>
```